Hummingfern Bramble Dabs - our own unique product line of cotton swabs

We have something now that we are not too happy with. Looking to create a label for a line of cotton swabs that we have created and designed to clean your nose from mucus and boogers. The logo that i have so far for the packaging is the white background with the black silhouette nose (attached). We need something that can do well in the retail/consumer market. Our website address (even though it is not live yet) should be listed somewhere on the label....
www.HummingfernBramble.example ( we sell pillows, but we have other product lines)
We would also like to see a brief description on how to correctly use the nose pick on the back side of the label. The description on how to use should read " insert cotton nose pick into nostril and give it a few counter clock wise twirls or till you feel mucus/debris latch onto the cotton. You may need to repeat the process and use more than one nose pick to achieve desired result."
As well as a warning mentioning : "Never insert plastic end of nose pick into any part of your body. Be careful and use with caution."
Also for you to know, the cotton is made from 100% natural cotton, the cotton head itself is thick and highly absorbent making it a pleasure to use. There are 50 nose picks per pack.
We're fine with keeping it simple and not making the packaging too busy, however we're open to your ideas and designs! I have given you the most important information relevant to the project. If there are any questions or something is not clear enough please kindly message me.

Requirements
Must have
• professional looking
clean looking
not busy
Should not have
• words clumping together making it appear as too much text in one area
too much text clumped together on the design

```html
<!DOCTYPE html>
<html lang="en">
<head>
<meta charset="utf-8">
<title>Hummingfern Bramble Dabs – Cotton Swabs Label</title>
<link rel="stylesheet" href="https://fonts.googleapis.com/css2?family=Ubuntu:wght@400&family=Montserrat:ital,wght@1,800;1,900&display=swap">
<style>
  :root {
    --brand-blue: #4573bb;
    --band-white: #ffffff;
    --band-lavender: #c3cdea;
    --backdrop: #e6e6e6;
    --illustration-tint: #dfe7f5;
  }
  html, body {
    margin: 0;
    padding: 0;
    width: 1200px;
    height: 895px;
    overflow: hidden;
    background: var(--backdrop);
  }
  .label {
    position: absolute;
    left: 132px;
    top: 47px;
    width: 935px;
    height: 800px;
    background: var(--brand-blue);
    overflow: hidden;
    box-shadow: 0 4px 14px rgba(0,0,0,0.18);
  }
  .label__waves {
    position: absolute;
    inset: 0;
    width: 100%;
    height: 100%;
  }
  .brand-lockup {
    position: absolute;
    right: 54px;
    top: 60px;
    width: 430px;
    text-align: center;
    color: var(--band-white);
    font-family: "Ubuntu", sans-serif;
    font-weight: 400;
  }
  .brand-lockup__name {
    font-size: 44px;
    line-height: 1.1;
    margin: 0;
  }
  .brand-lockup__line {
    font-size: 26px;
    letter-spacing: 8px;
    margin: 28px 0 0;
  }
  .nose-illustration {
    position: absolute;
    left: 36px;
    top: 220px;
    width: 320px;
    height: 470px;
    background: radial-gradient(ellipse at 55% 55%, var(--illustration-tint), rgba(223,231,245,0) 70%);
  }
  .product-type {
    position: absolute;
    left: 390px;
    top: 372px;
    width: 430px;
    text-align: center;
    color: var(--brand-blue);
    font-family: "Montserrat", sans-serif;
    font-style: italic;
  }
  .product-type__top {
    display: block;
    font-weight: 800;
    font-size: 50px;
    line-height: 1;
    letter-spacing: -1px;
  }
  .product-type__main {
    display: block;
    font-weight: 900;
    font-size: 98px;
    line-height: 1;
    letter-spacing: -1px;
    margin-top: 4px;
  }
  .web-address {
    position: absolute;
    right: 56px;
    bottom: 52px;
    color: var(--band-white);
    font-family: "Montserrat", sans-serif;
    font-style: italic;
    font-weight: 800;
    font-size: 25px;
  }
</style>
</head>
<body>
  <main class="label">
    <svg class="label__waves" viewBox="0 0 590 505" preserveAspectRatio="none" aria-hidden="true">
      <path fill="var(--band-lavender)" d="M0,50 C200,52 380,150 590,200 L590,218 C380,178 200,88 0,84 Z"/>
      <path fill="var(--band-white)" d="M0,80 C200,86 380,180 590,212 L590,290 C450,390 250,458 0,478 Z"/>
      <path fill="var(--band-lavender)" d="M590,265 C470,360 300,438 0,476 L0,480 C260,462 460,390 590,310 Z"/>
    </svg>

    <div class="brand-lockup">
      <p class="brand-lockup__name">Hummingfern Bramble</p>
      <p class="brand-lockup__line">Dabs</p>
    </div>

    <div class="nose-illustration" role="img" aria-label="Blue line illustration of a nose in profile"></div>

    <h1 class="product-type" style="margin:0">
      <span class="product-type__top">COTTON</span>
      <span class="product-type__main">SWABS</span>
    </h1>

    <p class="web-address" style="margin:0">www.HummingfernBramble.example</p>
  </main>
</body>
</html>
```